Web 2.0 my 1 page website ($500 Guaranteed)

Im looking for someone who can update my existing design at http://www.doriselvanby.com
I like existing layout and the way the boxes all work. Looking for the same design but with an updated web 2.0 textured look and feel.
Please note the current site is already working on top of pagecrate and new design needs to also work with pagecrate so I can continue to page content.
Looking for designer who can also get it working in pagecrate as it is today.
$500 AUD first prize for it all working.
If it helps:
I like minimailist. I like white. I like bright. I like texture. I like backgrounds. I like horizontal stripes running the length of the page. I like designs that work regardless of width of page. I like big bold statements. I like obvious. I like round edges. I like sites that look like they have come alive. I like depth. I like a 3D look. I like something very subtle that moves occassionally - just enough to catch your eye. I dont like popups. I dont like scrolling.
I like really clean SEO friendly source code. I like standards compatible design.
http://www.lotvessel.ie/ I like the depth of the mini coming out of the screen. I like the big bold fonts and the bright colours. I like the horizontal red stripe running the length of the page.
http://www.quillharbor.ie/ I like the backround clouds. I like the nice big lettering on the font on the mene bar. I like the nice bog boxes and contact numbers.
http://www.kuljepolkuja.fi/ I like the bright colours on the phone. I like the splash of the bubbles at the top of the page.
http://ontheruncue.me/ I like the blurred background. I REALLY like the rounded enter your email and notify me text boxes. I like the fonts on notify me and the textured background of the button.
http://9qtorn.com/it/ I really like the horizontal bar across the page - I like the big fonts in this background - I like the green and the orange. I really like the depth - how the beans and chair and butterfly sit on top of the page kind of bringing it to life. Like all the layers giving that illusion of 3D.
http://www.fenwrigley.net/ Like the big fonts, the horizontal bar, the leather stitching look around the "lets work together" and how everything is shadowed and sits off the page. I like the big contact us / get in touch / fonts at the bottom the big social media buttons. Probably this area could all be half the size but I like it.
http://www.drevoxis.com/ I like the graining textures in the background grays. I prefer blues and whites.
http://tibbinshedding.ca/ Like the big bold texts and the colours. Like the 3D cardboard box coming off the page.
http://pondchimers.com/ Like the textured backround - the rough grainy blue.
http://www.uk-rv.com/ I always liked those background kind of bursts behind the bay area picture in the middle. Like the striped blue background.
http://workshop.vendoqua.com/ Who doesnt like a ninja, but again like the big fonts and the way the person has depth
http://www.plumfolders.com/ I like the depth. I like the big bold colours.
http://www.5ibrelt.com/ Again like how the product is featured with lighting behind it, has that 3D look. Nice big lettering etc.
Updates
I like minimailist. I like white. I like bright. I like texture. I like
backgrounds. I like horizontal stripes running the length of the page. I
like designs that work regardless of width of page. I like big bold
statements. I like obvious. I like round edges. I like sites that look
like they have come alive. I like depth. I like a 3D look. I like
something very subtle that moves occassionally - just enough to catch
your eye. I dont like popups. I dont like scrolling.
http://www.lotvessel.ie/
I like the depth of the mini coming out of the screen. I like the big
bold fonts and the bright colours. I like the horizontal red stripe
running the length of the page.
http://www.quillharbor.ie/
I like the backround clouds. I like the nice big lettering on the font
on the mene bar. I like the nice bog boxes and contact numbers.
http://ontheruncue.me/
I like the blurred background. I REALLY like the rounded enter your
email and notify me text boxes. I like the fonts on notify me and the
textured background of the button.
http://9qtorn.com/it/
I really like the horizontal bar across the page - I like the big fonts
in this background - I like the green and the orange. I really like the
depth - how the beans and chair and butterfly sit on top of the page
kind of bringing it to life. Like all the layers giving that illusion of
3D.
http://www.fenwrigley.net/
Like the big fonts, the horizontal bar, the leather stitching look
around the "lets work together" and how everything is shadowed and sits
off the page. I like the big contact us / get in touch / fonts at the
bottom the big social media buttons. Probably this area could all be
half the size but I like it.
Typical Components of Web 2.0 Site Design
- Lots of space: Web 2.0 sites tend to have a lot of wide-open space. It's a contrast from the 90s, where the trend was to make usage of every square inch of a website's home page with links, banners and applets. White space is embraced to a major degree, as it calls attention to important buttons and links.
- The "Less Is More" Mentality: By putting less on the page, you're drawing more attention to the elements that matter: content and call-to-action buttons. "Clutter" and Web 2.0 simply do not mix - this is a new era of design psychology.
- Gradients: Merely a design element, gradients are used in Web 2.0 site design to give a clean, soft impression that's easy on the eyes.
- Large Fonts: Huge headings are a popular trend in Web 2.0 design - headings are usually taglines that describe or summarize what a website is about in just a handful of words. It's a huge benefit to first-timer usability, especially since new visitors would like to "get to the point" without having to read an intro paragraph.
- Dramatic Color Contrast: Another typical element seen in Web 2.0 design are bright colors (particularly neon colors) that accent site elements including menus, separator bars and footers. Many sites use this same neon color for their hyperlinks and headings, as well. Sometimes, the contrast between bright neon colors and charcoal or light gray text are put in unison for a dramatic effect.
- Eye Candy Logos: In Web 2.0 logo design, it's almost expected to see logos have a shiny plastic luster, or a soft gradient. Most Web 2.0 fonts are similar to basic Arial, Tahoma or Helvetica, and are simple. The colors used within the logo are also typically mimicked on other site design pieces to create a sense of uniformity.
- Huge Buttons: Calls to action (buttons that prompt you to "Get More Information," "Download Now," "See A Demo" or "Buy Now") are typically gigantic in Web 2.0 design. They're also attractive, featuring a color that strays away from the rest of the website's schematic. These buttons are typically isolated by a great deal of space, making them very easy to notice.
- Reflections: Product images, screenshots and icons can be seen as having "reflections" underneath them, as if they were standing on top of a new laminate floor. It's a stereotypical design element of Web 2.0.
- Lots of Icons: Web 2.0 icons are always in vector format, which is the standard format created by software such as Adobe Illustrator and Flash. They're attractive and clean looking, and are used to either draw attention to a website's sub-categories, a product's individual features, or anything else that the web designer wanted to help associate for a viewer.
- Exaggerated Web Form Fields: Huge form fields add to usability and draw attention to sign-ups and registrations. Instead of typing in a search, a username or anything else into a tiny web field, Web 2.0 has evolved them into massive interactive boxes with large text that makes things easy to see. For a good example, look at Glimvo.com's huge fields.

```html
<!DOCTYPE html>
<html lang="en">
<head>
<meta charset="utf-8">
<title>Doris Elvanby — Retail CIO</title>
<link rel="stylesheet" href="https://fonts.googleapis.com/css2?family=Cinzel:wght@700&family=Lora:wght@400;700&family=Open+Sans:wght@400;600&display=swap">
<style>
:root{
  --sky-top:#1b4f96;
  --sky-mid:#3f86cf;
  --sky-low:#7cb6e6;
  --ink-blue:#1a5aa8;
  --accent-cyan:#39b8f0;
  --panel-blue:rgba(92,104,190,.82);
  --panel-blue-head:rgba(70,80,165,.9);
  --welcome-top:#c25cc6;
  --welcome-low:#8c3aa6;
  --welcome-head:#a243b4;
  --charcoal:#2f2f31;
  --charcoal-low:#3c3c3e;
  --field:#59595c;
  --pink:#e4187c;
  --footer:#dcdcdc;
  --white:#ffffff;
}
*{box-sizing:border-box;margin:0;padding:0}
html,body{width:893px;height:1200px;overflow:hidden}
body{position:relative;font-family:"Open Sans",Arial,sans-serif;color:var(--white);
  background:linear-gradient(180deg,var(--sky-top) 0,var(--sky-mid) 330px,var(--sky-low) 750px)}
.abs{position:absolute}

.portrait{left:0;top:0;width:252px;height:195px;
  background:radial-gradient(ellipse at 50% 45%,#4f8fd6 0,#2a63a8 55%,#1b4f96 100%)}
.site-title{right:22px;top:22px;text-align:right}
.site-title .name{font-family:"Cinzel",Georgia,serif;font-size:40px;color:var(--white);letter-spacing:1px;text-shadow:0 2px 4px rgba(0,0,0,.35)}
.site-title .role{font-family:"Lora",Georgia,serif;font-weight:700;font-size:26px;color:var(--accent-cyan);margin-top:-4px}

.tagline{left:354px;top:138px;width:500px;height:86px;background:var(--white);border-radius:14px;
  box-shadow:0 4px 10px rgba(0,0,0,.3);display:flex;align-items:center;justify-content:center;
  padding:0 26px;text-align:center;font-size:12.5px;line-height:1.45;color:var(--ink-blue);font-weight:600;text-transform:uppercase}

.panel{background:var(--panel-blue);border-radius:10px;box-shadow:0 3px 8px rgba(0,0,0,.3);overflow:hidden}
.panel h2{font-family:"Lora",Georgia,serif;font-weight:400;font-size:21px;padding:4px 14px;background:var(--panel-blue-head)}
.panel p{font-size:8px;line-height:1.5;padding:6px 14px;color:#e6e8ff}
.tweets{left:28px;top:252px;width:408px;height:140px}
.interests{left:450px;top:252px;width:418px;height:140px}
.travel{left:28px;top:378px;width:408px;height:300px}
.career{left:450px;top:378px;width:418px;height:300px}
.travel p{width:135px}

.welcome{left:165px;top:400px;width:585px;height:318px;border-radius:12px;
  background:linear-gradient(180deg,var(--welcome-top),var(--welcome-low));box-shadow:0 8px 20px rgba(0,0,0,.45);overflow:hidden}
.welcome h1{font-family:"Lora",Georgia,serif;font-weight:400;font-size:36px;padding:6px 18px;background:var(--welcome-head)}
.welcome p{font-size:10.5px;line-height:1.55;padding:6px 18px 4px}
.welcome a{color:#ffd2f4;text-decoration:underline}

.toggle{left:424px;top:706px;width:54px;height:54px;z-index:3}

.contact-band{left:0;top:750px;width:893px;height:405px;
  background:linear-gradient(180deg,var(--charcoal),var(--charcoal-low));box-shadow:inset 0 6px 10px rgba(0,0,0,.4)}
.band-heading{font-family:"Open Sans",Arial,sans-serif;font-size:30px;font-weight:400}
.touch{left:24px;top:30px;width:440px}
.touch .sub{font-size:12px;margin-top:2px;color:#ddd}
.field-label{font-size:11px;color:#ddd}
.field{background:var(--field);border-radius:6px;border:1px solid #6a6a6e;box-shadow:inset 0 2px 4px rgba(0,0,0,.4)}
.submit{background:var(--pink);border-radius:6px;font-size:13px;font-weight:600;text-align:center;line-height:26px;letter-spacing:1px}

.contact-me{left:510px;top:30px;width:360px}
.contact-me .lorem{font-size:10px;line-height:1.45;margin-top:6px;color:#eee}
.row{display:flex;align-items:center;gap:14px;font-size:17px}
.row.social{font-size:20px}
.row.social .brand{color:var(--accent-cyan)}
.dot{width:46px;height:46px;border-radius:50%;background:#5a5a5e}

.footer{left:0;top:1155px;width:893px;height:45px;background:var(--footer);color:#555;
  font-size:11px;display:flex;align-items:center;justify-content:center}
</style>
</head>
<body>

<div class="abs portrait" role="img" aria-label="Portrait photo of the site owner in a blue shirt against a blue sky"></div>

<header class="abs site-title">
  <div class="name">DORIS ELVANBY</div>
  <div class="role">Retail CIO</div>
</header>

<div class="abs tagline">Australian retail CIO with a passion for multi-channel, multi-store technology. Specialise in using online communities to help drive the business by consumer engagement</div>

<section class="abs panel tweets"><h2>Tweets</h2>
  <p>Hello, and welcome to my home page on the web. There isn't really going to be much more here, just a brief and to the point summary of what I do and where I am heading next.</p></section>
<section class="abs panel interests"><h2>Current Interests</h2>
  <p>Hello, and welcome to my home page on the web. Lately my focus is online communities, store systems and the ways shoppers move between every channel we run.</p></section>
<section class="abs panel travel"><h2>Travelling Australia</h2>
  <p>Hello, and welcome to my home page. Right now I am on the road and sharing notes from each town along the coast, the outback and everything in between. More stops are added each week as I keep moving.</p></section>
<section class="abs panel career"><h2>Career Timeline</h2></section>

<article class="abs welcome">
  <h1>Welcome</h1>
  <p>Hello, and welcome to my home page on the web. There isn't really going to be much more here, just a brief summary and a way to reach me. For those that are interested in learning a bit more about me, connect on <a>Linkfolio</a> and feel free to click around and have a look.</p>
  <p>My background is basically a sales guy who a long time ago learnt how to use new technology to reach the masses. After running my own small computer business, I built my first commercial web site around 1999 and quickly moved into full blown online retail sites. Over the years I helped a number of stores grow by putting their customers first.</p>
  <p>In 2007 I went back into mainstream retail as the CIO at Harlow Home Centre, one of Australian largest franchisees. So I am looking for a new challenge where I can help a brand engage with people online.</p>
</article>

<svg class="abs toggle" viewBox="0 0 54 54" aria-hidden="true">
  <circle cx="27" cy="27" r="26" fill="#3a3a3c"/>
  <circle cx="27" cy="27" r="20" fill="#7a7a7e"/>
  <circle cx="27" cy="27" r="12" fill="#39b8f0"/>
</svg>

<section class="abs contact-band">
  <div class="abs touch">
    <h2 class="band-heading">Get in Touch...</h2>
    <div class="sub">If you have any queries, then send me a shout</div>
  </div>
  <div class="abs field-label" style="left:60px;top:98px">Name</div>
  <div class="abs field-label" style="left:280px;top:98px">E Mail</div>
  <div class="abs field" style="left:50px;top:92px;width:205px;height:26px"></div>
  <div class="abs field" style="left:268px;top:92px;width:190px;height:26px"></div>
  <div class="abs field" style="left:50px;top:134px;width:408px;height:26px"></div>
  <div class="abs field-label" style="left:60px;top:140px">Subject</div>
  <div class="abs field" style="left:50px;top:176px;width:408px;height:84px"></div>
  <div class="abs field-label" style="left:60px;top:184px">Message</div>
  <div class="abs submit" style="left:50px;top:272px;width:104px;height:26px">SUBMIT</div>

  <div class="abs contact-me">
    <h2 class="band-heading">Contact Me......</h2>
    <p class="lorem">Lorem ipsum dolor sit amet, consectetur adipiscing elit, sed do eiusmod tempor incididunt ut labore et dolore magna aliqua, ut enim ad minim veniam quis.</p>
  </div>
  <div class="abs row" style="left:520px;top:138px">
    <svg width="22" height="22" viewBox="0 0 24 24" aria-hidden="true"><path fill="#e4187c" d="M6.6 10.8a15 15 0 0 0 6.6 6.6l2.2-2.2a1 1 0 0 1 1-.25 11.4 11.4 0 0 0 3.6.57 1 1 0 0 1 1 1V20a1 1 0 0 1-1 1A17 17 0 0 1 3 4a1 1 0 0 1 1-1h3.5a1 1 0 0 1 1 1c0 1.25.2 2.45.57 3.57a1 1 0 0 1-.25 1z"/></svg>
    <span>555.0142.0142</span>
  </div>
  <div class="abs row" style="left:520px;top:180px;font-size:14px">
    <svg width="22" height="22" viewBox="0 0 24 24" aria-hidden="true"><rect x="2" y="5" width="20" height="14" rx="2" fill="#e4187c"/><path d="M3 6l9 7 9-7" fill="none" stroke="#fff" stroke-width="1.6"/></svg>
    <span>info@doriselvanby.com</span>
  </div>
  <div class="abs row social" style="left:520px;top:240px">
    <span class="dot"></span><span>Follow me on <span class="brand">Chatterly</span></span>
  </div>
  <div class="abs row social" style="left:520px;top:305px">
    <span class="dot"></span><span>Find me on <span class="brand">Friendloop</span></span>
  </div>
</section>

<footer class="abs footer">© 2011, All Rights Reserved, www.doriselvanby.com</footer>

</body>
</html>
```